Borealis Film and Design
Your Moments on Reels
Borealis Film and Design -
Creative Brief
Professional
Peter Vandrell
2187 Kettering Ln. Frostvale, Nordmark 99612
Peter@borealisfilmanddesign.example
borealisfilmanddesign.example

```html
<!DOCTYPE html>
<html lang="en">
<head>
<meta charset="utf-8">
<title>Borealis Film and Design – Stationery</title>
<link href="https://fonts.googleapis.com/css2?family=Montserrat:wght@700&family=Open+Sans:wght@400;600&display=swap" rel="stylesheet">
<style>
  :root {
    --bg: #e9eaec;
    --paper: #ffffff;
    --navy: #1c2a78;
    --blue: #2f45c8;
    --sky: #6f86e8;
    --ink: #3a3d48;
    --muted: #8a8e99;
    --faint: #e3e6ee;
    --dark: #1a1b21;
  }
  * { box-sizing: border-box; margin: 0; padding: 0; }
  html, body { width: 1200px; height: 343px; overflow: hidden; background: var(--bg); font-family: "Open Sans", sans-serif; color: var(--ink); }
  .canvas { position: relative; width: 1200px; height: 343px; }
  .piece { position: absolute; background: var(--paper); box-shadow: 0 1px 4px rgba(0,0,0,.25); overflow: hidden; }
  .caption { position: absolute; font-size: 5px; color: var(--muted); text-align: center; }

  .brand { font-family: "Montserrat", sans-serif; font-weight: 700; color: var(--navy); display: flex; align-items: center; gap: 3px; line-height: 1; white-space: nowrap; }
  .brand .dot { border-radius: 50%; background: var(--blue); flex: none; }
  .tagline { font-size: 4px; color: var(--muted); letter-spacing: .3px; }

  /* identity intro */
  .intro { position: absolute; left: 22px; top: 78px; }
  .intro .brand { font-size: 20px; }
  .intro .brand .dot { width: 14px; height: 14px; }
  .intro .label { font-size: 5px; color: var(--muted); margin-top: 8px; }

  /* business card */
  .card { left: 24px; top: 136px; width: 118px; height: 68px; }
  .card .brand { position: absolute; left: 7px; top: 8px; font-size: 9px; }
  .card .brand .dot { width: 7px; height: 7px; }
  .card .person { position: absolute; left: 7px; top: 24px; font-size: 4.4px; line-height: 1.4; }
  .card .person b { font-weight: 600; color: var(--navy); }
  .card .contact { position: absolute; left: 46px; top: 23px; width: 68px; font-size: 3px; line-height: 1.55; color: var(--ink); white-space: nowrap; }
  .card .band { position: absolute; left: 0; bottom: 0; width: 100%; height: 20px; }

  /* letterhead */
  .letter { top: 19px; width: 216px; height: 274px; }
  .letter .brand { position: absolute; left: 14px; top: 16px; font-size: 13px; }
  .letter .brand .dot { width: 10px; height: 10px; }
  .letter .tagline { position: absolute; left: 14px; top: 31px; }
  .letter .contact { position: absolute; right: 12px; top: 14px; font-size: 3.6px; line-height: 1.5; text-align: left; width: 64px; }
  .watermark { position: absolute; left: 68px; top: 92px; width: 80px; height: 80px; border-radius: 50%; background: var(--faint); opacity: .8; }
  .letter .band { position: absolute; left: 0; bottom: 0; width: 100%; height: 36px; }
  .letter .footer { position: absolute; left: 0; bottom: 5px; width: 100%; font-size: 3.6px; color: #fff; text-align: center; white-space: nowrap; }

  /* envelope front */
  .env { left: 638px; width: 231px; height: 88px; }
  .env .brand { position: absolute; left: 10px; top: 10px; font-size: 10px; }
  .env .brand .dot { width: 8px; height: 8px; }
  .env .tagline { position: absolute; left: 10px; top: 22px; font-size: 3.4px; }
  .env .band { position: absolute; left: 0; bottom: 0; width: 100%; height: 22px; }
  .env .address { position: absolute; left: 10px; top: 27px; font-size: 3.4px; line-height: 1.5; color: var(--muted); }

  /* envelope back */
  .back { left: 893px; width: 288px; height: 84px; }
  .back svg { position: absolute; inset: 0; }
</style>
</head>
<body>
<div class="canvas">

  <div class="intro">
    <div class="brand"><span>BOREALIS</span><span class="dot"></span></div>
    <div class="label">Stationery Concept</div>
  </div>

  <div class="piece card">
    <div class="brand"><span>BOREALIS</span><span class="dot"></span></div>
    <div class="person"><b>Peter Vandrell</b><br>Professional</div>
    <div class="contact">2187 Kettering Ln.<br>Frostvale, Nordmark 99612<br>Peter@borealisfilmanddesign.example<br>borealisfilmanddesign.example</div>
    <svg class="band" viewBox="0 0 118 20" preserveAspectRatio="none" aria-hidden="true">
      <path d="M0 8 Q60 -2 118 10 V20 H0Z" fill="var(--sky)"/>
      <path d="M0 11 Q60 3 118 13 V20 H0Z" fill="var(--navy)"/>
    </svg>
  </div>
  <div class="caption" style="left:24px;top:212px;width:118px">Business Card</div>

  <div class="piece letter" style="left:168px">
    <div class="brand"><span>BOREALIS</span><span class="dot"></span></div>
    <div class="tagline">Your Moments on Reels</div>
    <div class="contact">Borealis Film and Design<br>2187 Kettering Ln.<br>Frostvale, Nordmark 99612<br>borealisfilmanddesign.example</div>
    <div class="watermark"></div>
    <svg class="band" viewBox="0 0 216 36" preserveAspectRatio="none" aria-hidden="true">
      <path d="M0 14 Q108 0 216 16 V36 H0Z" fill="var(--sky)"/>
      <path d="M0 19 Q108 8 216 21 V36 H0Z" fill="var(--navy)"/>
    </svg>
    <div class="footer">borealisfilmanddesign.example</div>
  </div>
  <div class="caption" style="left:168px;top:298px;width:216px">Letterhead</div>

  <div class="piece letter" style="left:403px">
    <div class="watermark"></div>
    <svg class="band" viewBox="0 0 216 36" preserveAspectRatio="none" aria-hidden="true">
      <path d="M0 14 Q108 0 216 16 V36 H0Z" fill="var(--sky)"/>
      <path d="M0 19 Q108 8 216 21 V36 H0Z" fill="var(--navy)"/>
    </svg>
    <div class="footer">2187 Kettering Ln. Frostvale, Nordmark 99612 · Peter@borealisfilmanddesign.example</div>
  </div>
  <div class="caption" style="left:403px;top:298px;width:216px">Letterhead</div>

  <div class="piece env" style="top:132px">
    <div class="brand"><span>BOREALIS</span><span class="dot"></span></div>
    <div class="tagline">Your Moments on Reels</div>
    <div class="address">2187 Kettering Ln.<br>Frostvale, Nordmark 99612</div>
    <svg class="band" viewBox="0 0 231 22" preserveAspectRatio="none" aria-hidden="true">
      <path d="M0 10 Q115 2 231 12 V22 H0Z" fill="var(--sky)"/>
      <path d="M0 13 Q115 6 231 15 V22 H0Z" fill="var(--navy)"/>
    </svg>
  </div>
  <div class="caption" style="left:638px;top:224px;width:231px">Envelope</div>

  <div class="piece env" style="top:240px">
    <svg class="band" viewBox="0 0 231 22" preserveAspectRatio="none" aria-hidden="true">
      <path d="M0 10 Q115 2 231 12 V22 H0Z" fill="var(--sky)"/>
      <path d="M0 13 Q115 6 231 15 V22 H0Z" fill="var(--navy)"/>
    </svg>
  </div>
  <div class="caption" style="left:638px;top:331px;width:231px">Envelope</div>

  <div class="piece back" style="top:128px">
    <svg viewBox="0 0 288 84" aria-hidden="true">
      <rect width="288" height="84" fill="var(--paper)"/>
      <path d="M0 84 L144 38 L288 84" fill="none" stroke="#d4d6dc" stroke-width=".8"/>
      <path d="M0 0 H288 L144 44 Z" fill="var(--dark)"/>
      <path d="M0 0 L144 44 L288 0" fill="none" stroke="var(--blue)" stroke-width="1.5"/>
      <circle cx="144" cy="38" r="7" fill="var(--blue)" stroke="#fff" stroke-width="1"/>
    </svg>
  </div>

  <div class="piece back" style="top:232px;height:90px">
    <svg viewBox="0 0 288 90" aria-hidden="true">
      <rect width="288" height="90" fill="var(--paper)"/>
      <path d="M0 0 L144 46 L288 0" fill="#f3f4f7" stroke="#c9ccd4" stroke-width=".8"/>
      <path d="M0 90 L144 42 L288 90" fill="none" stroke="#d4d6dc" stroke-width=".8"/>
      <circle cx="144" cy="40" r="7" fill="var(--blue)" stroke="#fff" stroke-width="1"/>
    </svg>
  </div>

</div>
</body>
</html>
```